Architectural firm needs a graphic representation of our Master Planning process

We need an image to convey our 3-phase, 8-step Master Planning process that we utilize when designing plans for schools K-12. What we currently use looks very outdated in both the design and color scheme. We'd like an EPS created that can be scaled without distortion. The files I've attached show the current graphic and an instruction sheet which also contains our colors.

```html
<!DOCTYPE html>
<html lang="en">
<head>
<meta charset="utf-8">
<title>Planning Process</title>
<link href="https://fonts.googleapis.com/css2?family=Lato:wght@300;400;700;900&display=swap" rel="stylesheet">
<style>
  :root {
    --bg: #efefef;
    --process-blue: #236a9c;
    --school: #0f4b63;
    --architect: #a21d33;
    --fundraising: #aaa23a;
    --ink: #1c1c1c;
    --footer-bg: #2c2c2c;
    --footer-text: #f2f2f2;
    --white: #ffffff;
  }
  * { margin: 0; padding: 0; box-sizing: border-box; }
  html, body { width: 1200px; height: 2305px; overflow: hidden; background: var(--bg); }
  .canvas {
    position: relative; width: 1200px; height: 2305px;
    background: var(--bg); font-family: "Lato", Arial, sans-serif; color: var(--ink);
  }
  .diagram { position: absolute; left: 0; top: 0; }
  .title {
    position: absolute; left: 567px; top: 100px;
    color: var(--process-blue); font-weight: 900; line-height: 1;
  }
  .title-line-1 { display: block; font-size: 100px; letter-spacing: 2px; }
  .title-line-2 { display: block; font-size: 100px; letter-spacing: 14px; margin-top: 10px; }
  .step-label {
    position: absolute; left: 568px; font-size: 52px; font-weight: 400;
    line-height: 1.04; transform: translateY(-50%); text-transform: uppercase;
  }
  .footer {
    position: absolute; left: 0; top: 2024px; width: 1200px; height: 281px;
    background: var(--footer-bg); color: var(--footer-text);
  }
  .footer-note {
    position: absolute; left: 28px; top: 16px;
    font-size: 29.5px; font-weight: 300; line-height: 41.5px;
  }
  .legend { position: absolute; left: 922px; top: 10px; }
  .legend-item { display: flex; align-items: center; height: 88px; }
  .legend-dot { width: 74px; height: 74px; border-radius: 50%; flex: none; opacity: 0.85; }
  .legend-dot.school { background: var(--school); }
  .legend-dot.architect { background: var(--architect); }
  .legend-dot.fundraising { background: var(--fundraising); }
  .legend-label { margin-left: 4px; font-size: 21px; font-weight: 400; line-height: 1.3; text-transform: uppercase; }
</style>
</head>
<body>
<div class="canvas">
  <svg class="diagram" width="1200" height="2024" viewBox="0 0 1200 2024">
    <!-- process spine -->
    <line x1="486" y1="0" x2="486" y2="1913" stroke="var(--process-blue)" stroke-width="3"/>
    <!-- role lanes -->
    <line x1="109" y1="115" x2="109" y2="1913" stroke="var(--school)" stroke-width="3"/>
    <line x1="223" y1="115" x2="223" y2="1913" stroke="var(--architect)" stroke-width="3"/>
    <line x1="335" y1="115" x2="335" y2="1913" stroke="var(--fundraising)" stroke-width="3"/>
    <!-- role badges -->
    <circle cx="109" cy="115" r="45" fill="var(--school)" role="img" aria-label="School icon"/>
    <circle cx="223" cy="115" r="45" fill="var(--architect)" role="img" aria-label="Architect icon"/>
    <circle cx="335" cy="115" r="45" fill="var(--fundraising)" role="img" aria-label="Fundraising consultant icon"/>

    <!-- responsibility markers -->
    <g class="markers-school" fill="var(--school)">
      <circle cx="109" cy="527" r="11"/><circle cx="109" cy="1454" r="11"/><circle cx="109" cy="1913" r="11"/>
    </g>
    <g class="markers-architect" fill="var(--architect)">
      <circle cx="223" cy="527" r="11"/><circle cx="223" cy="764" r="11"/><circle cx="223" cy="1006" r="11"/>
      <circle cx="223" cy="1223" r="11"/><circle cx="223" cy="1454" r="11"/><circle cx="223" cy="1684" r="11"/>
      <circle cx="223" cy="1913" r="11"/>
    </g>
    <g class="markers-fundraising" fill="var(--fundraising)">
      <circle cx="335" cy="527" r="11"/><circle cx="335" cy="1454" r="11"/><circle cx="335" cy="1913" r="11"/>
    </g>

    <!-- step nodes -->
    <g fill="var(--process-blue)">
      <circle cx="486" cy="527" r="66"/><circle cx="486" cy="764" r="66"/><circle cx="486" cy="993" r="66"/>
      <circle cx="486" cy="1223" r="66"/><circle cx="486" cy="1454" r="66"/><circle cx="486" cy="1684" r="66"/>
      <circle cx="486" cy="1913" r="66"/>
    </g>

    <!-- icon: lightbulb -->
    <g transform="translate(486 527)" fill="none" stroke="var(--white)" stroke-width="4" stroke-linecap="round">
      <path d="M-10 14 C-10 4 -20 0 -20 -12 A20 20 0 0 1 20 -12 C20 0 10 4 10 14 Z"/>
      <line x1="-9" y1="21" x2="9" y2="21"/><line x1="-7" y1="28" x2="7" y2="28"/>
      <line x1="0" y1="-44" x2="0" y2="-38"/><line x1="-32" y1="-12" x2="-40" y2="-12"/><line x1="32" y1="-12" x2="40" y2="-12"/>
      <line x1="-23" y1="-35" x2="-28" y2="-40"/><line x1="23" y1="-35" x2="28" y2="-40"/>
      <line x1="-26" y1="10" x2="-32" y2="15"/><line x1="26" y1="10" x2="32" y2="15"/>
    </g>
    <!-- icon: house with magnifier -->
    <g transform="translate(486 764)" fill="var(--white)">
      <path d="M-44 0 L-8 -32 L22 -6 L22 -2 L14 -2 L-8 -22 L-32 -1 L-32 30 L-6 30 L-6 36 L-38 36 L-38 4 Z"/>
      <rect x="-22" y="10" width="12" height="20"/>
      <circle cx="16" cy="16" r="14" fill="none" stroke="var(--white)" stroke-width="6"/>
      <line x1="26" y1="26" x2="42" y2="42" stroke="var(--white)" stroke-width="8" stroke-linecap="round"/>
    </g>
    <!-- icon: exclamation -->
    <g transform="translate(486 993)" fill="var(--white)">
      <path d="M-9 -44 H9 L5 16 H-5 Z"/><circle cx="0" cy="33" r="9"/>
    </g>
    <!-- icon: puzzle piece -->
    <g transform="translate(486 1223)" fill="var(--white)">
      <path d="M-30 -32 H-8 A10 10 0 1 1 10 -32 H30 V-12 A10 10 0 1 1 30 6 V30 H8 A10 10 0 1 0 -10 30 H-30 V8 A10 10 0 1 0 -30 -10 Z" transform="rotate(12)"/>
    </g>
    <!-- icon: tick -->
    <g transform="translate(486 1454)">
      <polyline points="-34,2 -10,26 34,-24" fill="none" stroke="var(--white)" stroke-width="13" stroke-linecap="round" stroke-linejoin="round"/>
    </g>
    <!-- icon: document -->
    <g transform="translate(486 1684)" fill="none" stroke="var(--white)" stroke-width="5">
      <path d="M-26 -38 H14 L28 -24 V38 H-26 Z" stroke-linejoin="round"/>
      <line x1="-15" y1="-14" x2="17" y2="-14"/><line x1="-15" y1="-2" x2="17" y2="-2"/>
      <line x1="-15" y1="10" x2="17" y2="10"/><line x1="-15" y1="22" x2="17" y2="22"/>
    </g>
    <!-- icon: gears -->
    <g transform="translate(486 1913)" fill="var(--white)">
      <circle cx="-12" cy="6" r="18"/>
      <circle cx="-12" cy="6" r="25" fill="none" stroke="var(--white)" stroke-width="10" stroke-dasharray="8 7"/>
      <circle cx="-12" cy="6" r="8" fill="var(--process-blue)"/>
      <circle cx="26" cy="-20" r="9"/>
      <circle cx="26" cy="-20" r="13" fill="none" stroke="var(--white)" stroke-width="6" stroke-dasharray="5 4.3"/>
      <circle cx="26" cy="-20" r="4" fill="var(--process-blue)"/>
      <circle cx="26" cy="28" r="9"/>
      <circle cx="26" cy="28" r="13" fill="none" stroke="var(--white)" stroke-width="6" stroke-dasharray="5 4.3"/>
      <circle cx="26" cy="28" r="4" fill="var(--process-blue)"/>
    </g>
  </svg>

  <h1 class="title">
    <span class="title-line-1">PLANNING</span>
    <span class="title-line-2">PROCESS</span>
  </h1>

  <div class="step-label" style="top:527px">Visioning</div>
  <div class="step-label" style="top:764px">Space &amp; Physical<br>Conditions Assessment</div>
  <div class="step-label" style="top:993px">Problem Defined</div>
  <div class="step-label" style="top:1217px">Identify Solutions</div>
  <div class="step-label" style="top:1450px">Assess &amp; Select</div>
  <div class="step-label" style="top:1680px">Compile Report</div>
  <div class="step-label" style="top:1908px">Implement Plan!</div>

  <footer class="footer">
    <p class="footer-note">
      Image above depicts a general outline of the process<br>
      developed by R&amp;M and used when conducting facilities<br>
      master plans. The areas of responsibility are shown a<br>
      circle for the group under a step, yet the groups<br>
      (especially the school and the architect) are always<br>
      working together towards the goal.
    </p>
    <div class="legend">
      <div class="legend-item"><span class="legend-dot school" role="img" aria-label="School icon"></span><span class="legend-label">School</span></div>
      <div class="legend-item"><span class="legend-dot architect" role="img" aria-label="Architect icon"></span><span class="legend-label">Architect</span></div>
      <div class="legend-item"><span class="legend-dot fundraising" role="img" aria-label="Fundraising consultant icon"></span><span class="legend-label">Fundraising<br>Consultant</span></div>
    </div>
  </footer>
</div>
</body>
</html>
```